Steward Compass - Descriptive Diagram/Graphic of Concepts

Steward Compass is a personal change philosophy that focuses on the individual making six commitments - Authenticity, Curiosity, Vision, Passion, Courage, and Humility - and living a cycle of Balance, Sustainability, and Renewal. In a typical business presentation, the Six Commitments would be displayed as a pyramid (Authenticity as the Foundation, Humility as the pinnacle) and the cycle likely a circle with each concept running into each other.

The challenge then is two fold. I need a graphical representation of those concepts, but I need it integrated, so that the cycle supports the commitments. I am open to ideas but it should be something that can be used for print or graphic materials, as well as presented on a website. Colors do not matter, but it sould be colorful.

Industry/Entity Type

Graphic Design

```html
<!DOCTYPE html>
<html lang="en">
<head>
<meta charset="utf-8">
<title>Steward Compass – Commitments and Cycle</title>
<link rel="stylesheet" href="https://fonts.googleapis.com/css2?family=Tinos&display=swap">
<style>
  :root {
    --page: #ffffff;
    --frame: #8a7553;
    --frame-edge: #5e4f37;
    --cycle-word: #c6ae85;
    --cycle-shade: rgba(50, 38, 20, 0.75);
    --band-1: #dcd0ba;
    --band-2: #d3c6ae;
    --band-3: #cbbda2;
    --band-4: #c3b396;
    --band-5: #bba98b;
    --band-6: #b3a081;
    --commitment-ink: #141210;
  }
  html, body {
    margin: 0;
    padding: 0;
    width: 1200px;
    height: 1200px;
    overflow: hidden;
    background: var(--page);
  }
  .diagram {
    display: block;
    width: 1200px;
    height: 1200px;
  }
  .cycle-frame {
    fill: var(--frame);
    stroke: var(--frame-edge);
    stroke-width: 2;
  }
  .commitment-field {
    stroke: #e9e0cf;
    stroke-width: 2;
    fill: none;
  }
  .band-1 { fill: var(--band-1); }
  .band-2 { fill: var(--band-2); }
  .band-3 { fill: var(--band-3); }
  .band-4 { fill: var(--band-4); }
  .band-5 { fill: var(--band-5); }
  .band-6 { fill: var(--band-6); }
  .cycle-word {
    font-family: "Tinos", "Times New Roman", serif;
    fill: var(--cycle-word);
    filter: drop-shadow(-2px 2px 1px var(--cycle-shade));
  }
  .commitment {
    font-family: "Tinos", "Times New Roman", serif;
    fill: var(--commitment-ink);
    text-anchor: middle;
  }
</style>
</head>
<body>
<svg class="diagram" viewBox="0 0 1200 1200" xmlns="http://www.w3.org/2000/svg" role="img" aria-label="Six commitments stacked inside a triangle framed by the cycle of Renewal, Balance and Sustainability">
  <defs>
    <clipPath id="commitment-clip">
      <polygon points="604,350 255,881 950,881"/>
    </clipPath>
  </defs>

  <polygon class="cycle-frame" points="604,112 24,998 1178,998"/>

  <g class="cycle-words">
    <text class="cycle-word" x="363" y="580" font-size="104" text-anchor="middle" textLength="590" lengthAdjust="spacingAndGlyphs" transform="rotate(-56.8 363 580)" dy="34">Renewal</text>
    <text class="cycle-word" x="832" y="580" font-size="104" text-anchor="middle" textLength="590" lengthAdjust="spacingAndGlyphs" transform="rotate(56.8 832 580)" dy="34">Balance</text>
    <text class="cycle-word" x="606" y="964" font-size="96" text-anchor="middle" textLength="985" lengthAdjust="spacingAndGlyphs">Sustainability</text>
  </g>

  <g class="commitment-bands" clip-path="url(#commitment-clip)">
    <rect class="band-1" x="240" y="340" width="720" height="157"/>
    <rect class="band-2" x="240" y="497" width="720" height="73"/>
    <rect class="band-3" x="240" y="570" width="720" height="82"/>
    <rect class="band-4" x="240" y="652" width="720" height="78"/>
    <rect class="band-5" x="240" y="730" width="720" height="73"/>
    <rect class="band-6" x="240" y="803" width="720" height="80"/>
  </g>
  <polygon class="commitment-field" points="604,350 255,881 950,881"/>

  <g class="commitments">
    <text class="commitment" x="604" y="481" font-size="32">Humility</text>
    <text class="commitment" x="604" y="549" font-size="40">Courage</text>
    <text class="commitment" x="604" y="629" font-size="49">Passion</text>
    <text class="commitment" x="604" y="712" font-size="58">Vision</text>
    <text class="commitment" x="604" y="782" font-size="57">Curiosity</text>
    <text class="commitment" x="604" y="859" font-size="58">Authenticity</text>
  </g>
</svg>
</body>
</html>
```